Ember Quill Vitamin and Supplements site

I would like a design for vitamin and supplements website that will only stock the very best products. These vitamins will expensive. It needs to look distinct from the various vitamin, health and beauty websites. It needs to be simple and elegant, unisex, and with a mild/slight scientific feel. I will be choosing my products that are sold on my site based on great reviews and the tested science behind the products. This rigour should be reflected in the look and feel of the site.

I have a separate project for the coding the website, however I need further ideas on the design itself.

Target Market(s)

This site is for people who are willing to try new things and care deeply about their health.

Industry/Entity Type

Health And Wellness

```html
<!DOCTYPE html>
<html lang="en">
<head>
<meta charset="utf-8">
<title>Ember Quill Vitamin &amp; Supplements</title>
<link href="https://fonts.googleapis.com/css2?family=Roboto:wght@400;500;700&display=swap" rel="stylesheet">
<style>
:root{
  --navy:#0d3a6e;
  --green:#9cc31f;
  --text:#444;
  --dark:#3a3a3a;
  --white:#fff;
}
*{margin:0;padding:0;box-sizing:border-box}
html,body{width:1200px;height:2625px;overflow:hidden}
body{position:relative;font-family:'Roboto',Arial,sans-serif;color:var(--text);background:var(--white)}
.abs{position:absolute}

/* header */
.site-header{left:0;top:0;width:1200px;height:70px;background:var(--white)}
.brand{left:107px;top:20px;display:flex;align-items:center;gap:12px}
.brand-dot{width:26px;height:26px;border-radius:50%;background:var(--navy)}
.brand-name{font-size:24px;font-weight:500;color:var(--navy);letter-spacing:.5px}
.main-nav{right:110px;top:28px;display:flex;gap:46px;font-size:14px;font-weight:500}
.main-nav a{color:#333;text-decoration:none}
.main-nav a.active{color:var(--green)}

/* hero */
.hero-photo{left:0;top:70px;width:1200px;height:800px;
  background:linear-gradient(180deg,rgba(255,255,255,0) 70%,#fff 100%),
  linear-gradient(90deg,#e9eef0 0%,#f3f3f3 25%,#e6e2dc 55%,#b7a48b 75%,#5b5450 100%)}
.hero-note{left:107px;font-size:22px;font-weight:500;line-height:28px;color:#444;width:190px}
.note-dot{width:28px;height:28px;border-radius:50%}
.products-btn{left:512px;top:318px;width:176px;height:68px;border-radius:34px;background:var(--navy);
  color:var(--white);font-size:26px;font-weight:700;display:flex;align-items:center;justify-content:center}
.section-title{width:1200px;left:0;text-align:center;color:var(--navy);font-weight:700;font-size:40px}
.mission-text{left:110px;top:789px;width:980px;font-size:20px;font-weight:500;line-height:25.7px;text-align:justify;color:#444;letter-spacing:.3px}

/* research */
.research-bg{left:0;top:987px;width:1200px;height:800px;
  background:linear-gradient(90deg,#ecebe8 0%,#f7f7f6 30%,#f8f8f8 70%,#eceae7 100%)}
.research-img{top:1080px;width:468px;height:342px}
.research-img.molecule{left:104px;background:radial-gradient(circle at 60% 40%,#2a7fbf,#0d4a87 70%)}
.research-img.capsule{left:625px;background:linear-gradient(135deg,#cfe6f6 0%,#4aa0dc 50%,#0f5fa8 100%)}
.research-title{top:1448px;width:500px;text-align:center;font-size:27px;font-weight:700;color:var(--navy)}
.research-text{top:1483px;width:482px;font-size:19.5px;font-weight:500;line-height:25.5px;color:#444;text-align:justify;letter-spacing:.2px}
.green-btn{top:1657px;width:166px;height:47px;background:var(--green);color:var(--white);
  font-size:22px;font-weight:500;display:flex;align-items:center;justify-content:center}
.research-note{left:105px;top:1722px;width:990px;text-align:center;font-size:19.5px;font-weight:500;line-height:26px;color:#444;letter-spacing:.25px}

/* breeds */
.breed-img{top:1895px;height:225px}
.breed-img.horses{left:104px;width:318px;background:linear-gradient(180deg,#dce8ef 0%,#c9a27f 60%,#8a5a35 100%)}
.breed-img.rabbits{left:445px;width:308px;background:linear-gradient(180deg,#6f7e55 0%,#cfcfcb 50%,#2f5a23 100%)}
.breed-img.cats{left:776px;width:320px;background:linear-gradient(180deg,#e2e2e2 0%,#8a8d90 55%,#c9c9c9 100%)}
.arrow{top:1983px}
.breed-name{top:2155px;width:318px;text-align:center;font-size:22px;font-weight:500;color:#555}
.breed-text{top:2207px;width:305px;font-size:17px;font-weight:500;line-height:28px;color:#555;letter-spacing:.45px}
.navy-btn{width:118px;height:37px;background:var(--navy);color:var(--white);font-size:17px;font-weight:700;
  display:flex;align-items:center;justify-content:center}

/* footer */
.site-footer{left:0;top:2466px;width:1200px;height:159px;background:var(--dark)}
.footer-brand{left:118px;top:2506px;display:flex;align-items:center;gap:22px}
.footer-brand .brand-dot{width:46px;height:46px;background:var(--green)}
.footer-brand .brand-name{color:var(--white);font-size:28px;line-height:36px}
.footer-nav{right:72px;top:2527px;display:flex;gap:60px;font-size:20px;font-weight:700}
.footer-nav a{color:var(--white);text-decoration:none}
.footer-nav a.active{color:var(--green)}
.social{right:72px;top:2573px;display:flex;gap:9px}
.social span{width:27px;height:27px;border-radius:4px;background:var(--white)}
</style>
</head>
<body>

<header class="abs site-header">
  <div class="abs brand"><span class="brand-dot"></span><span class="brand-name">Ember Quill Vitamin &amp; Supplements</span></div>
  <nav class="abs main-nav">
    <a class="active" href="#">ABOUT US</a><a href="#">RESEARCHES</a><a href="#">BLOG</a><a href="#">CONTACT US</a>
  </nav>
</header>

<div class="abs hero-photo" role="img" aria-label="Photo of a small white dog in a lab coat and a pug at a microscope in a bright laboratory"></div>
<span class="abs note-dot" style="left:108px;top:141px;background:var(--navy)"></span>
<p class="abs hero-note" style="top:182px">Take the blue pill and find out what science discover</p>
<span class="abs note-dot" style="left:108px;top:299px;background:var(--green)"></span>
<p class="abs hero-note" style="top:342px">Take the green pill and find out what animals discover</p>
<div class="abs products-btn">PRODUCTS</div>

<h2 class="abs section-title" style="top:730px">MISSION</h2>
<p class="abs mission-text">Why science is important. Contrary to popular belief, Lorem Ipsum is not simply random text. It has roots in a piece of classical Latin literature from 45 BC, making it over 2000 years old. Tobias Wrenfield, a Latin professor at Alder Vale College in Oregon, looked up one of the more obscure Latin words, consectetur, from a Lorem Ipsum passage, and going through the cites of the word in classical literature, discovered the undoubtable source. Lorem Ipsum comes from sections 1.10.32 and 1.10.33 of "de Finibus.</p>

<div class="abs research-bg" role="img" aria-label="Faded laboratory background with a microscope"></div>
<h2 class="abs section-title" style="top:1002px;font-size:39px">MOST RECENT RESEARCHES</h2>
<div class="abs research-img molecule" role="img" aria-label="Blue glass molecule model"></div>
<div class="abs research-img capsule" role="img" aria-label="Open capsule releasing small granules on blue"></div>

<h3 class="abs research-title" style="left:97px">SCIENCE POINT OF VIEW</h3>
<p class="abs research-text" style="left:109px">It is a long established fact that a reader will be distracted by the readable content of a page when looking at its layout. The point of using Lorem Ipsum is that it has a more-or-less normal distribution of letters, as opposed to using 'Content here, content here', making it look like readable English. And so on.</p>
<a class="abs green-btn" style="left:265px">Find more</a>

<h3 class="abs research-title" style="left:605px">ALL SUPPLEMENTS ANALISIS</h3>
<p class="abs research-text" style="left:616px">It is a long established fact that a reader will be distracted by the readable content of a page when looking at its layout. The point of using Lorem Ipsum is that it has a more-or-less normal distribution of letters, as opposed to using 'Content here, content here', making it look like readable English. And so on.</p>
<a class="abs green-btn" style="left:771px">Find more</a>

<p class="abs research-note">There are many variations of passages of Lorem Ipsum available, but the majority have suffered alteration in some form, by injected humour, or randomised words which don't look even slightly believable.</p>

<h2 class="abs section-title" style="top:1818px;font-size:39px">DIFFERENT BREED</h2>
<svg class="abs arrow" style="left:53px" width="32" height="36" viewBox="0 0 32 36"><polygon points="32,0 32,36 0,18" fill="#9cc31f"/></svg>
<svg class="abs arrow" style="left:1116px" width="32" height="36" viewBox="0 0 32 36"><polygon points="0,0 0,36 32,18" fill="#9cc31f"/></svg>
<div class="abs breed-img horses" role="img" aria-label="Photo of a brown and white pony"></div>
<div class="abs breed-img rabbits" role="img" aria-label="Photo of a white and grey rabbit on grass"></div>
<div class="abs breed-img cats" role="img" aria-label="Photo of a grey cat yawning"></div>

<h4 class="abs breed-name" style="left:110px">HORSES</h4>
<p class="abs breed-text" style="left:120px">Lorem Ipsum has been the industry's standard dummy text ever since the 1500s, when an unknown printer took a galley of type and scrambled it to make a type specimen book. More...</p>
<a class="abs navy-btn" style="left:210px;top:2384px">FIND MORE</a>

<h4 class="abs breed-name" style="left:440px">RABBITS</h4>
<p class="abs breed-text" style="left:451px">Lorem Ipsum has been the industry's standard dummy text ever since the 1500s, when an unknown printer took a galley of type and scrambled it to make a type specimen book. More...</p>
<a class="abs navy-btn" style="left:540px;top:2386px">FIND MORE</a>

<h4 class="abs breed-name" style="left:771px">CATS</h4>
<p class="abs breed-text" style="left:782px">Lorem Ipsum has been the industry's standard dummy text ever since the 1500s, when an unknown printer took a galley of type and scrambled it to make a type specimen book. More...</p>
<a class="abs navy-btn" style="left:871px;top:2386px">FIND MORE</a>

<footer class="abs site-footer"></footer>
<div class="abs footer-brand"><span class="brand-dot"></span><span class="brand-name">Ember Quill Vitamin<br>&amp; Supplements</span></div>
<nav class="abs footer-nav">
  <a class="active" href="#">ABOUT US</a><a href="#">RESEARCHES</a><a href="#">BLOG</a><a href="#">CONTACT US</a>
</nav>
<div class="abs social" aria-label="Social links"><span></span><span></span><span></span></div>

</body>
</html>
```